ALL TYPES OF COMMERCIAL PLASTERING

TYPE OF BLOCK LETTERING WITH STAND OUT QUALITIES
WITH SOME TYPE OF LOGO
SOMETHING UNIQUE FOR THE BUILDING INDUSTRY.
QUALITY WORKMANSHIP
Updates

forgot to include my mobile phone number on my brief. could you add it to your design please MOBILE PH 0418 695 031

please let me make this quite clear ,the company name is northgate linings and Fitouts PTY LTD. THE TYPE OF WORK WE WILL BE DOING IS COMMERCIAL PLASTERING.

Industry/Entity Type

Industry

Contact Information for Business Card

northgate linings and fitouts P/L
martin corbell p.o.box 42 wendouree 3355 email address northgatelinings@mailbox-example.com
ABN 51 847 213 906 COMMERCIAL PLASTERING

```html
<!DOCTYPE html>
<html lang="en">
<head>
<meta charset="utf-8">
<title>northgate linings and fitouts P/L — business card</title>
<link rel="stylesheet" href="https://fonts.googleapis.com/css2?family=Heebo:wght@300;400&display=swap">
<style>
  :root {
    --stage: #d9d4cc;
    --card: #060606;
    --ink: #f2f2f2;
    --ink-soft: #d8d8d8;
  }
  * { margin: 0; padding: 0; box-sizing: border-box; }
  html, body { width: 1200px; height: 800px; overflow: hidden; }
  body {
    background: var(--stage);
    display: flex;
    align-items: center;
    justify-content: center;
    font-family: "Heebo", Arial, sans-serif;
  }
  .business-card {
    position: relative;
    width: 900px;
    height: 514px;
    background: var(--card);
    color: var(--ink);
    border-radius: 6px;
    box-shadow: 0 18px 40px rgba(0,0,0,0.35);
  }
  .brand {
    position: absolute;
    left: 190px;
    top: 78px;
    display: flex;
    align-items: center;
    gap: 22px;
  }
  .brand-mark {
    width: 110px;
    height: 110px;
    border-radius: 50%;
    border: 5px solid var(--ink);
    flex: none;
  }
  .brand-name {
    font-weight: 400;
    font-size: 40px;
    line-height: 1.02;
    letter-spacing: 2px;
    text-transform: uppercase;
  }
  .brand-tagline {
    display: block;
    margin-top: 8px;
    font-size: 17px;
    letter-spacing: 1.5px;
    font-weight: 300;
  }
  .holder-name {
    position: absolute;
    left: 84px;
    top: 232px;
    font-weight: 300;
    font-size: 36px;
    letter-spacing: 0.5px;
  }
  .contact-list {
    position: absolute;
    left: 60px;
    top: 300px;
    list-style: none;
  }
  .contact-item {
    display: flex;
    align-items: center;
    gap: 22px;
    height: 36px;
    font-weight: 300;
    font-size: 22px;
    color: var(--ink-soft);
  }
  .contact-item svg {
    width: 22px;
    height: 22px;
    flex: none;
    fill: var(--ink);
  }
</style>
</head>
<body>
  <section class="business-card">
    <div class="brand">
      <span class="brand-mark"></span>
      <div class="brand-name">
        northgate linings<br>and fitouts P/L
        <span class="brand-tagline">commercial plastering</span>
      </div>
    </div>

    <p class="holder-name">martin corbell</p>

    <ul class="contact-list">
      <li class="contact-item">
        <svg viewBox="0 0 24 24" aria-hidden="true"><path d="M7 1h10a2 2 0 0 1 2 2v18a2 2 0 0 1-2 2H7a2 2 0 0 1-2-2V3a2 2 0 0 1 2-2zm0 3v13h10V4H7zm5 15a1.3 1.3 0 1 0 0 2.6 1.3 1.3 0 0 0 0-2.6z"/></svg>
        0418 695 031
      </li>
      <li class="contact-item">
        <svg viewBox="0 0 24 24" aria-hidden="true"><path d="M12 1a8 8 0 0 0-8 8c0 6 8 14 8 14s8-8 8-14a8 8 0 0 0-8-8zm0 11a3 3 0 1 1 0-6 3 3 0 0 1 0 6z"/></svg>
        ABN 51 847 213 906
      </li>
      <li class="contact-item">
        <svg viewBox="0 0 24 24" aria-hidden="true"><path d="M12 2 1 12h3v10h6v-6h4v6h6V12h3z"/></svg>
        p.o.box 42 wendouree 3355
      </li>
      <li class="contact-item">
        <svg viewBox="0 0 24 24" aria-hidden="true"><path d="M2 5h20v14H2zm2 2v.5l8 5.5 8-5.5V7zm0 3v7h16v-7l-8 5.5z"/></svg>
        northgatelinings@mailbox-example.com
      </li>
    </ul>
  </section>
</body>
</html>
```